Stationary package for Real Estate Brokerage Ambervale Homes inc
Ambervale Homes - Brokerage Independently Owned and Operated
Stationary package for Real Estate Brokerage Ambervale Homes inc - Real Estate
Creative Brief
Modern
Delia Marchetti
Sales Representative
42 Calderwood Avenue, Ottawa, ON, K2P 3R6
delia_marchetti@quillmail.example
www.deliamarchetti.example
Space for personal photo (head shot) in the front
Office address and extra details on the back

```html
<!DOCTYPE html>
<html lang="en">
<head>
<meta charset="utf-8">
<title>Ambervale Homes stationery</title>
<link href="https://fonts.googleapis.com/css2?family=Cinzel:wght@600&family=Open+Sans:wght@400;600;700&display=swap" rel="stylesheet">
<style>
  :root{
    --backdrop:#9b6a29;
    --paper:#ffffff;
    --ink:#3a3a3a;
    --muted:#8a8a8a;
    --gold:#9a7a45;
    --gold-soft:#e9dcc3;
    --rule:#c9c9c9;
    --map:#eef0f3;
  }
  *{box-sizing:border-box;margin:0;padding:0}
  html,body{width:1200px;height:995px;overflow:hidden}
  body{background:var(--backdrop);font-family:"Open Sans",Arial,sans-serif;color:var(--ink);position:relative}
  .sheet{position:absolute;background:var(--paper);box-shadow:0 3px 10px rgba(0,0,0,.3);overflow:hidden}
  .world-map{position:absolute;background:radial-gradient(ellipse at 50% 50%,var(--map) 0%,rgba(238,240,243,.5) 60%,rgba(255,255,255,0) 100%)}
  .brand{display:flex;align-items:center;gap:6px;font-family:"Cinzel",Georgia,serif;font-weight:600;color:var(--ink);white-space:nowrap}
  .brand-dot{border-radius:50%;border:2px solid var(--gold);flex:none}
  .brand-rule{height:2px;background:var(--gold)}
  .small{font-size:7px;line-height:1.45;color:var(--muted);white-space:nowrap}
  .footer-rule{position:absolute;left:14px;right:14px;height:1px;background:var(--gold)}

  /* business cards */
  .card{width:300px;height:170px}
  .card-front{left:40px;top:170px}
  .card-back{left:40px;top:360px}
  .headshot{position:absolute;left:18px;top:78px;width:52px;height:64px;background:linear-gradient(#cfc6bb,#8f8377)}
  .card-name{position:absolute;left:84px;top:80px;font-size:11px;font-weight:700}
  .card-role{position:absolute;left:84px;top:95px;font-size:8px;color:var(--gold)}
  .card-contact{position:absolute;left:84px;top:110px}
  .card-front .brand{position:absolute;left:18px;top:22px;font-size:15px}
  .card-back .brand{position:absolute;left:34px;top:58px;font-size:24px}
  .card-back .tagline{position:absolute;left:34px;top:98px;font-size:8px;color:var(--gold);letter-spacing:.5px}
  .card-back .card-contact{left:34px;top:124px}

  /* letterhead */
  .letterhead{left:375px;top:40px;width:255px;height:360px}
  .letterhead .brand{position:absolute;left:16px;top:18px;font-size:15px}
  .letterhead .header-contact{position:absolute;right:14px;top:16px;text-align:right}
  .letterhead-footer{position:absolute;left:14px;bottom:10px}

  /* envelope */
  .envelope{left:660px;top:40px;width:500px;height:230px}
  .envelope .brand{position:absolute;left:20px;top:20px;font-size:16px}
  .envelope .return{position:absolute;left:20px;top:50px}

  /* fax + invoice */
  .form{top:430px;width:370px;height:525px}
  .fax{left:375px}
  .invoice{left:790px}
  .form .brand{position:absolute;left:20px;top:22px;font-size:17px}
  .form-title{position:absolute;right:20px;top:24px;font-size:14px;font-weight:700;letter-spacing:1px;color:var(--ink)}
  .fax-table{position:absolute;left:20px;top:90px;width:330px;border-collapse:collapse;font-size:8px}
  .fax-table th{background:var(--gold);color:#fff;text-align:left;padding:4px 6px;font-weight:600}
  .fax-table td{border:1px solid var(--rule);padding:5px 6px;height:22px;color:var(--muted)}
  .checks{position:absolute;left:20px;top:272px;display:flex;gap:12px;font-size:8px;color:var(--muted)}
  .checks span::before{content:"";display:inline-block;width:7px;height:7px;border:1px solid var(--muted);margin-right:4px;vertical-align:-1px}
  .invoice-meta{position:absolute;left:20px;top:70px;width:330px}
  .invoice-meta div{border-bottom:1px solid var(--rule);height:16px;font-size:7.5px;color:var(--muted);padding-top:3px}
  .invoice-table{position:absolute;left:20px;top:130px;width:330px;border-collapse:collapse;font-size:8px}
  .invoice-table th{background:var(--gold);color:#fff;padding:4px 6px;font-weight:600;text-align:left}
  .invoice-table td{border-left:1px solid var(--rule);border-right:1px solid var(--rule);border-bottom:1px solid #e6e6e6;height:14px}
  .invoice-total{position:absolute;right:20px;top:442px;font-size:8px;font-weight:700}
  .invoice-thanks{position:absolute;left:20px;top:462px;font-size:7.5px;color:var(--muted)}
  .form-footer{position:absolute;left:20px;bottom:16px}
  .form-footer-right{position:absolute;right:20px;bottom:16px;text-align:right}
</style>
</head>
<body>

  <section class="sheet card card-front">
    <div class="world-map" style="left:120px;top:10px;width:180px;height:110px" role="img" aria-label="Faint world map decoration"></div>
    <div class="brand"><span class="brand-dot" style="width:12px;height:12px"></span>Ambervale Homes</div>
    <div class="headshot" role="img" aria-label="Space for agent head shot photo"></div>
    <div class="card-name">Delia Marchetti</div>
    <div class="card-role">Sales Representative</div>
    <div class="card-contact small">Cell: 613-555-0148<br>delia_marchetti@quillmail.example<br>www.deliamarchetti.example</div>
  </section>

  <section class="sheet card card-back">
    <div class="world-map" style="left:140px;top:20px;width:160px;height:130px" role="img" aria-label="Faint world map decoration"></div>
    <div class="brand"><span class="brand-dot" style="width:18px;height:18px"></span>Ambervale Homes</div>
    <div class="brand-rule" style="position:absolute;left:34px;top:92px;width:210px"></div>
    <div class="tagline">Brokerage Independently Owned and Operated</div>
    <div class="card-contact small">42 Calderwood Avenue, Ottawa, ON, K2P 3R6<br>Office: 613-555-0100 &nbsp; Fax: 613-555-0199</div>
  </section>

  <section class="sheet letterhead">
    <div class="world-map" style="left:20px;top:80px;width:220px;height:150px" role="img" aria-label="Faint world map decoration"></div>
    <div class="brand"><span class="brand-dot" style="width:12px;height:12px"></span>Ambervale Homes</div>
    <div class="brand-rule" style="position:absolute;left:16px;top:42px;width:120px"></div>
    <div class="header-contact small">T 613-555-0100<br>F 613-555-0199<br>C 613-555-0148</div>
    <div class="footer-rule" style="bottom:36px"></div>
    <div class="letterhead-footer small">42 Calderwood Avenue, Ottawa, ON, K2P 3R6<br>www.deliamarchetti.example</div>
  </section>

  <section class="sheet envelope">
    <div class="world-map" style="left:150px;top:30px;width:300px;height:170px" role="img" aria-label="Faint world map decoration"></div>
    <div class="brand"><span class="brand-dot" style="width:13px;height:13px"></span>Ambervale Homes</div>
    <div class="return small">Delia Marchetti, Sales Representative<br>42 Calderwood Avenue, Ottawa, ON, K2P 3R6</div>
    <div class="footer-rule" style="bottom:22px;left:20px;right:20px"></div>
  </section>

  <section class="sheet form fax">
    <div class="world-map" style="left:40px;top:150px;width:300px;height:220px" role="img" aria-label="Faint world map decoration"></div>
    <div class="brand"><span class="brand-dot" style="width:14px;height:14px"></span>Ambervale Homes</div>
    <div class="brand-rule" style="position:absolute;left:20px;top:50px;width:150px"></div>
    <div class="form-title">FAX</div>
    <table class="fax-table">
      <tr><th colspan="4">Fax Transmission</th></tr>
      <tr><td>To:</td><td></td><td>From:</td><td></td></tr>
      <tr><td>Fax:</td><td></td><td>Pages:</td><td></td></tr>
      <tr><td>Phone:</td><td></td><td>Date:</td><td></td></tr>
      <tr><td>Re:</td><td></td><td>CC:</td><td></td></tr>
      <tr><td colspan="4">Comments:</td></tr>
    </table>
    <div class="checks"><span>Urgent</span><span>For Review</span><span>Please Comment</span><span>Please Reply</span></div>
    <div class="footer-rule" style="bottom:38px;left:20px;right:20px"></div>
    <div class="form-footer small">42 Calderwood Avenue, Ottawa, ON, K2P 3R6</div>
    <div class="form-footer-right small">T 613-555-0100 &nbsp; F 613-555-0199</div>
  </section>

  <section class="sheet form invoice">
    <div class="world-map" style="left:40px;top:150px;width:300px;height:220px" role="img" aria-label="Faint world map decoration"></div>
    <div class="brand"><span class="brand-dot" style="width:14px;height:14px"></span>Ambervale Homes</div>
    <div class="form-title">INVOICE</div>
    <div class="invoice-meta"><div>Bill to:</div><div>Invoice No:</div><div>Date:</div></div>
    <table class="invoice-table">
      <tr><th style="width:40px">Qty</th><th>Description</th><th style="width:60px">Price</th><th style="width:60px">Amount</th></tr>
      <tr><td></td><td></td><td></td><td></td></tr><tr><td></td><td></td><td></td><td></td></tr>
      <tr><td></td><td></td><td></td><td></td></tr><tr><td></td><td></td><td></td><td></td></tr>
      <tr><td></td><td></td><td></td><td></td></tr><tr><td></td><td></td><td></td><td></td></tr>
      <tr><td></td><td></td><td></td><td></td></tr><tr><td></td><td></td><td></td><td></td></tr>
      <tr><td></td><td></td><td></td><td></td></tr><tr><td></td><td></td><td></td><td></td></tr>
      <tr><td></td><td></td><td></td><td></td></tr><tr><td></td><td></td><td></td><td></td></tr>
      <tr><td></td><td></td><td></td><td></td></tr><tr><td></td><td></td><td></td><td></td></tr>
      <tr><td></td><td></td><td></td><td></td></tr><tr><td></td><td></td><td></td><td></td></tr>
      <tr><td></td><td></td><td></td><td></td></tr>
    </table>
    <div class="invoice-total">Total:</div>
    <div class="invoice-thanks">Thank you for your business.</div>
    <div class="footer-rule" style="bottom:38px;left:20px;right:20px"></div>
    <div class="form-footer small">42 Calderwood Avenue, Ottawa, ON, K2P 3R6</div>
    <div class="form-footer-right small">T 613-555-0100 &nbsp; F 613-555-0199</div>
  </section>

</body>
</html>
```